Simple and Approachable Cover for Pet Expo Company Page

Size: 2000 x 430; looking simply for words "Dunmore HR Consulting" and email address "DunmoreHRConsulting@brelvamail.com." This is for a cover photo for a company profile page for the Hollow Oak Expo, where I am a featured speaker on Employee Communications later this month. You can incorporate the attached photo to the left of the banner ad if you wish. The mood I wish to present is approachable, positive and simple.

Target Market(s)

small pet retail business owners

Industry/Entity Type

Pet Shop

Font styles to use
Serif
Sans Serif

Requirements
Must have
• Email address clearly defined/separated. Easy to read.
Nice to have
• I like the picture that I included; subtle pet paw background is also nice
Should not have
• No paid stock images

```html
<!DOCTYPE html>
<html lang="en">
<head>
<meta charset="utf-8">
<title>Dunmore HR Consulting — Cover Banner</title>
<link href="https://fonts.googleapis.com/css2?family=Abhaya+Libre:wght@800&family=Open+Sans:wght@400&display=swap" rel="stylesheet">
<style>
  :root {
    --page-bg: #f4f8f9;
    --banner-teal: #008272;
    --accent-peach: #f9c487;
    --photo-tone-a: #c98a55;
    --photo-tone-b: #7a8fb0;
    --photo-tone-c: #d2383f;
  }
  html, body {
    margin: 0;
    padding: 0;
    width: 1200px;
    height: 1000px;
    overflow: hidden;
    background: var(--page-bg);
  }
  .cover-banner {
    position: absolute;
    left: 29px;
    top: 378px;
    width: 1142px;
    height: 245px;
    background: var(--banner-teal);
  }
  .team-photo {
    position: absolute;
    left: 38px;
    top: 16px;
    width: 384px;
    height: 229px;
    border-radius: 120px 120px 0 0;
    background: radial-gradient(ellipse at 50% 70%, var(--photo-tone-c) 0%, var(--photo-tone-a) 40%, var(--photo-tone-b) 75%, rgba(0,130,114,0) 100%);
    opacity: 0.85;
  }
  .company-name {
    position: absolute;
    left: 368px;
    top: 48px;
    width: 704px;
    margin: 0;
    text-align: right;
    font-family: "Abhaya Libre", Georgia, serif;
    font-weight: 800;
    font-size: 58px;
    letter-spacing: 1px;
    line-height: 1;
    color: var(--accent-peach);
  }
  .contact-email {
    position: absolute;
    left: 368px;
    top: 153px;
    width: 704px;
    margin: 0;
    text-align: right;
    font-family: "Open Sans", Arial, sans-serif;
    font-weight: 400;
    font-size: 29px;
    letter-spacing: 0.5px;
    line-height: 1;
    color: var(--accent-peach);
  }
</style>
</head>
<body>
  <header class="cover-banner">
    <div class="team-photo" role="img" aria-label="Photo of the two consultants seated with their two beagle dogs"></div>
    <h1 class="company-name">Dunmore HR Consulting</h1>
    <p class="contact-email">DunmoreHRConsulting@brelvamail.com</p>
  </header>
</body>
</html>
```